Letterhead design for business

Looking for an attractive and professional letterhead that uses the logo that is attached below.

Target Market(s)

Potential bankruptcy clients.

Industry/Entity Type

Legal

Colors

Designer to choose colors to be used in the design.

Requirements
Must have
• Address for locations, phone number, and website address.
• Addresses are on website ferncoveadvice.example. Use following phone number (for tracking purposes): 555-013-8274

```html
<!DOCTYPE html>
<html lang="en">
<head>
<meta charset="utf-8">
<title>Ferncove Advice – Letterhead</title>
<link rel="stylesheet" href="https://fonts.googleapis.com/css2?family=Open+Sans:wght@400;600&family=Arimo:wght@700&display=swap">
<style>
  :root {
    --backdrop: #e4e5e7;
    --paper: #f8f8f8;
    --ink: #3a3a3a;
    --heading-ink: #111111;
    --brand-green: #86bd7f;
    --brand-green-dark: #6aa563;
    --footer-dark: #414042;
    --footer-text: #ffffff;
  }
  * { box-sizing: border-box; margin: 0; padding: 0; }
  html, body {
    width: 1200px; height: 945px; overflow: hidden;
    background: var(--backdrop);
  }
  .letterhead {
    position: absolute; left: 285px; top: 27px;
    width: 630px; height: 891px;
    background: var(--paper);
    box-shadow: 0 2px 10px rgba(0,0,0,0.12);
    overflow: hidden;
    font-family: "Open Sans", sans-serif;
    color: var(--ink);
  }
  .brand {
    position: absolute; left: 58px; top: 44px;
    display: flex; align-items: center; gap: 10px;
  }
  .brand-mark {
    width: 34px; height: 34px; border-radius: 50%;
    background: var(--brand-green);
  }
  .brand-name {
    font-size: 22px; font-weight: 600; color: var(--brand-green-dark);
    line-height: 1;
  }
  .brand-byline {
    position: absolute; left: 102px; top: 76px;
    font-size: 7px; color: var(--brand-green-dark); letter-spacing: 0.3px;
  }
  .salutation {
    position: absolute; left: 90px; top: 150px;
    font-family: "Arimo", sans-serif; font-weight: 700;
    font-size: 14px; color: var(--heading-ink);
  }
  .letter-body {
    position: absolute; left: 90px; top: 180px; width: 470px;
    font-size: 12px; line-height: 1.4;
  }
  .letter-body p { margin-bottom: 12px; }
  .signature {
    position: absolute; left: 95px; top: 622px;
    width: 130px; height: 42px; border-radius: 4px;
    background: linear-gradient(90deg, #e6e6e6, #d9d9d9);
  }
  .footer-wave {
    position: absolute; left: 0; bottom: 0; width: 630px; height: 260px;
  }
  .contact {
    position: absolute; left: 48px; bottom: 18px;
    list-style: none; color: var(--footer-text);
    font-size: 11px; line-height: 15px;
  }
  .contact li { display: flex; align-items: flex-start; gap: 7px; }
  .contact svg { width: 10px; height: 10px; margin-top: 2.5px; flex: none; }
  .contact .address-lines { display: block; }
</style>
</head>
<body>
  <main class="letterhead">
    <header class="brand">
      <span class="brand-mark"></span>
      <span class="brand-name">Ferncove Advice</span>
    </header>
    <p class="brand-byline">by Attorney M. Lindqvist</p>

    <p class="salutation">Dear Mr. Adams,</p>

    <section class="letter-body">
      <p>Lorem Ipsum is simply dummy text of the printing and typesetting industry. Lorem Ipsum has been the industry's standard dummy text ever since the 1500s, when an unknown printer took a galley of type and scrambled it to make a type specimen book. It has survived not only five centuries, but also the leap into electronic typesetting, remaining essentially unchanged.</p>
      <p>The standard chunk of Lorem Ipsum used since the 1500s is reproduced below for those interested. Sections 1.10.32 and 1.10.33 from "de Finibus Bonorum et Malorum" by Cicero are also reproduced in their exact original form, accompanied by English versions from the 1914 translation by H. Rackham</p>
      <p>Lorem Ipsum is simply dummy text of the printing and typesetting industry. Lorem Ipsum has been the industry's standard dummy text ever since the 1500s, when an unknown printer took a galley of type and scrambled it to make a type specimen book. It has survived not only five centuries, but also the leap into electronic typesetting, remaining essentially unchanged. It was popularised in the</p>
      <p>The standard chunk of Lorem Ipsum used since the 1500s is reproduced below for those interested. Sections 1.10.32 and 1.10.33 from "de Finibus Bonorum et Malorum" by Cicero are also reproduced in their exact original form, accompanied by English versions from the 1914 translation by H. Rackham</p>
      <p>The standard chunk of Lorem Ipsum used since the 1500s is reproduced below for those interested. Sections 1.10.32 and 1.10.33 from "de Finibus Bonorum et Malorum" by Cicero are</p>
    </section>

    <div class="signature" role="img" aria-label="Handwritten signature of the attorney"></div>

    <svg class="footer-wave" viewBox="0 0 630 260" preserveAspectRatio="none" aria-hidden="true">
      <path d="M0,130 C150,75 300,120 430,92 C530,70 600,30 630,0" fill="none" stroke="var(--brand-green)" stroke-width="7"/>
      <path d="M0,146 C150,92 300,136 430,108 C530,86 600,46 630,16" fill="none" stroke="var(--brand-green)" stroke-width="12"/>
      <path d="M0,260 V158 C150,104 300,148 430,120 C530,98 600,58 630,28 V260 Z" fill="var(--footer-dark)"/>
    </svg>

    <ul class="contact">
      <li>
        <svg viewBox="0 0 10 10"><path d="M2 0.5 L3.8 2.6 L2.9 3.8 C3.5 5.2 4.8 6.5 6.2 7.1 L7.4 6.2 L9.5 8 L8.3 9.5 C4.5 9.2 0.8 5.5 0.5 1.7 Z" fill="var(--brand-green)"/></svg>
        555-013-8274
      </li>
      <li>
        <svg viewBox="0 0 10 10"><rect x="0.5" y="2" width="9" height="6.5" fill="var(--brand-green)"/><path d="M0.5 2 L5 5.6 L9.5 2" fill="none" stroke="var(--footer-dark)" stroke-width="0.9"/></svg>
        help@ferncoveadvice.example
      </li>
      <li>
        <svg viewBox="0 0 10 10"><circle cx="5" cy="5" r="4.3" fill="none" stroke="var(--brand-green)" stroke-width="1.1"/><ellipse cx="5" cy="5" rx="1.8" ry="4.3" fill="none" stroke="var(--brand-green)" stroke-width="0.9"/><path d="M0.7 5 H9.3" stroke="var(--brand-green)" stroke-width="0.9"/></svg>
        www.ferncoveadvice.example
      </li>
      <li>
        <svg viewBox="0 0 10 10"><path d="M5 0.3 C2.6 0.3 1.2 2 1.2 3.9 C1.2 6.4 5 9.8 5 9.8 C5 9.8 8.8 6.4 8.8 3.9 C8.8 2 7.4 0.3 5 0.3 Z" fill="var(--brand-green)"/><circle cx="5" cy="3.9" r="1.4" fill="var(--footer-dark)"/></svg>
        <span class="address-lines">12 Alder Row Westfield 3091 Harbourtown Australia<br>4120 E. Mill St. Brookhaven, Georgia 30999</span>
      </li>
    </ul>
  </main>
</body>
</html>
```